Business Card Design

I am a mental health counselor in private practice. I provide counseling to individuals, couples, and adults. There is a design on CardLoom that I really like. It is 2 talking bubbles joined together by a heart. That is just a suggestion. I'm interested in other ideas. I would like my photo to be on the back of the card, along with the text Miriam Delacott Counseling. I would like mint green as my background color and navy writing, if possible. The final design should be elegant, professional, and maybe just a touch whimsical.
Target Market(s)
Individual adolescents, adults, couples, and families seeking counseling.
Industry/Entity Type
Mental Health
Contact Information for Business Card
Miriam Delacott
A Wholehearted Approach to Counseling
Miriam Delacott, M.S. NCC
Wexmoor Hall
2947 NW Calloway Street, Suite 318
Portland OR 97209
503-286-1573
counselingwithmiriam-example.com
Requirements
Must have
- The card must have all of the text provided and my photo.
Nice to have
- I like cards that are rounded on the sides, and I like thick paper.

```html
<!DOCTYPE html>
<html lang="en">
<head>
<meta charset="utf-8">
<title>Miriam Delacott Counseling – Business Card</title>
<link href="https://fonts.googleapis.com/css2?family=Open+Sans:wght@300;400;600;700&display=swap" rel="stylesheet">
<style>
  :root {
    --forest: #06352a;
    --mint: #86d9ca;
    --paper: #ffffff;
    --backdrop: #ece8e2;
    --photo-dark: #2a2a2a;
    --photo-light: #e9d9b8;
  }
  * { box-sizing: border-box; margin: 0; padding: 0; }
  html, body {
    width: 1200px; height: 845px; overflow: hidden;
    background: var(--backdrop);
    font-family: "Open Sans", sans-serif;
  }
  .canvas { position: relative; width: 1200px; height: 845px; }

  .card {
    position: absolute;
    width: 680px; height: 390px;
    border-radius: 34px;
    overflow: hidden;
    box-shadow: 0 6px 18px rgba(0,0,0,.18);
  }

  /* Front */
  .card-front { left: 40px; top: 25px; background: var(--paper); }
  .front-panel {
    position: absolute; left: 0; top: 0; width: 100%; height: 305px;
    background: var(--forest);
  }
  .brand-title {
    position: absolute; left: 220px; top: 46px;
    color: var(--mint); font-size: 23px; font-weight: 300; letter-spacing: .3px;
    white-space: nowrap;
  }
  .brand-title strong { font-weight: 700; }
  .tagline {
    position: absolute; left: 222px; top: 80px;
    color: var(--mint); font-size: 11.5px; font-weight: 600; letter-spacing: .5px;
    text-transform: uppercase;
  }
  .mark {
    position: absolute; left: 36px; top: 150px;
    display: flex; align-items: center; gap: 8px;
    color: var(--mint); font-size: 16px; font-weight: 700;
  }
  .mark-dot { width: 20px; height: 20px; border-radius: 50%; background: var(--mint); }
  .contact-row {
    position: absolute; left: 240px;
    display: flex; gap: 12px; align-items: flex-start;
    color: var(--mint); font-size: 14.5px; font-weight: 600; line-height: 1.5;
  }
  .contact-address { top: 168px; }
  .contact-phone { top: 248px; }
  .contact-row svg { flex: none; margin-top: 2px; }
  .front-url {
    position: absolute; left: 0; right: 0; top: 325px;
    text-align: center; padding-left: 60px;
    color: var(--forest); font-size: 18px; font-weight: 700; letter-spacing: 2.5px;
  }

  /* Back */
  .card-back { left: 480px; top: 435px; background: var(--mint); }
  .back-title {
    position: absolute; left: 36px; top: 192px;
    color: var(--forest); font-size: 18px; font-weight: 700; letter-spacing: .2px;
    white-space: nowrap;
  }
  .back-url {
    position: absolute; left: 72px; top: 220px;
    color: var(--forest); font-size: 12px; font-weight: 600;
  }
  .portrait {
    position: absolute; left: 415px; top: 40px; width: 245px; height: 350px;
    border-radius: 120px 120px 0 0;
    background: linear-gradient(180deg, var(--photo-light) 0%, var(--photo-light) 55%, var(--photo-dark) 75%, var(--photo-dark) 100%);
  }
</style>
</head>
<body>
<main class="canvas">

  <section class="card card-front">
    <div class="front-panel">
      <h1 class="brand-title">MIRIAM DELACOTT <strong>COUNSELING</strong></h1>
      <p class="tagline">A Wholehearted Approach to Counseling</p>

      <div class="mark"><span class="mark-dot"></span>Miriam Delacott</div>

      <div class="contact-row contact-address">
        <svg width="18" height="20" viewBox="0 0 20 22" aria-hidden="true">
          <rect x="0" y="0" width="20" height="22" rx="3" fill="var(--mint)"/>
          <path d="M10 4a5 5 0 0 0-5 5c0 4 5 9 5 9s5-5 5-9a5 5 0 0 0-5-5z" fill="var(--forest)"/>
          <circle cx="10" cy="9" r="2" fill="var(--mint)"/>
        </svg>
        <p>Miriam Delacott,<br>M.S. NCC Wexmoor Hall 2947 NW Calloway Street,<br>Suite 318 Portland OR 97209</p>
      </div>

      <div class="contact-row contact-phone">
        <svg width="18" height="18" viewBox="0 0 20 20" aria-hidden="true">
          <rect x="0" y="0" width="20" height="20" rx="3" fill="var(--mint)"/>
          <path d="M6 4l2.5 3-1.5 1.5c.8 1.8 2.2 3.2 4 4l1.5-1.5 3 2.5-1.5 2.5C9 16 4 11 3.5 5.5z" fill="var(--forest)"/>
        </svg>
        <p>503-286-1573</p>
      </div>
    </div>
    <p class="front-url">www.counselingwithmiriam-example.com</p>
  </section>

  <section class="card card-back">
    <h2 class="back-title">MIRIAM DELACOTT COUNSELING</h2>
    <p class="back-url">www.counselingwithmiriam-example.com</p>
    <div class="portrait" role="img" aria-label="Portrait photo of the counselor, smiling, with shoulder-length blonde hair"></div>
  </section>

</main>
</body>
</html>
```